Hi! We require a design for business cards for directors and head teachers of an international daycare for children 0 - 9. We are family-owned, -operated and -oriented. We have six locations, looking to franchise. Our USPs are: 1) Flexibility 2) Quality teachers 3) International culture 4) Best nutrition We are quality teachers and professional caretakers, but with creativity and personality! Business cards should be playful (but no Comic Sans or baby hand prints), colorful (but no rainbows), and have some breathing space. It should be obvious from the business card that we're a daycare. In 2020 we'll be launching our new website based on this design: https://plomvane.io/47K2RQLWZTD The font in the new website will be Houschka (medium, demibold, bold). We will keep our current logo, included in the files here. There are also screenshots of some designs we like. Show us your best! :)

Industry/Entity Type

Childcare

Contact Information for Business Card

Lotte de Vries-Bakhuis
Communications Wizard
Poppel Hoek International Daycare
Kastanjeweg 47 B, 2316 KR Leiden
www.poppelhoek.nl
+31 647315082

Font styles to use
Serif
Sans Serif

Colors

Designer to choose colors to be used in the design.

Requirements
Must have
• Color

```html
<!DOCTYPE html>
<html lang="en">
<head>
<meta charset="utf-8">
<title>Poppel Hoek – Business Card</title>
<link href="https://fonts.googleapis.com/css2?family=Ubuntu:wght@400;500;700&display=swap" rel="stylesheet">
<style>
  :root {
    --stage: #e6e6e8;
    --pink: #d93d7a;
    --blue: #1aa0d8;
    --blue-soft: #6cc7ea;
    --white: #ffffff;
    --paper: #f4f4f5;
    --ink-white: #ffffff;
    --shadow: rgba(0,0,0,0.18);
  }
  * { margin: 0; padding: 0; box-sizing: border-box; }
  html, body { width: 1200px; height: 1021px; overflow: hidden; }
  body {
    background: var(--stage);
    font-family: "Ubuntu", sans-serif;
    position: relative;
  }
  .card {
    position: absolute;
    left: 220px;
    width: 760px;
    height: 434px;
    border-radius: 4px;
    overflow: hidden;
    box-shadow: 0 10px 28px var(--shadow);
  }
  /* Front */
  .card-front { top: 44px; background: var(--pink); }
  .front-art { position: absolute; border-radius: 50%; }
  .art-balloon-left { left: 70px; top: 110px; width: 80px; height: 90px; background: var(--blue-soft); }
  .art-balloon-right { left: 600px; top: 95px; width: 115px; height: 120px; background: #f19bc0; }
  .art-cloud-left { left: 110px; top: 300px; width: 120px; height: 52px; border-radius: 30px; background: #f6eef2; }
  .art-cloud-right { left: 540px; top: 350px; width: 120px; height: 52px; border-radius: 30px; background: #f6eef2; }
  .art-comet { left: 70px; top: 40px; width: 140px; height: 50px; border-radius: 25px; background: linear-gradient(90deg, #7fd0d8, #f4d84a); }
  .art-characters-front {
    position: absolute; left: 290px; top: 100px; width: 180px; height: 80px;
    border-radius: 40px 40px 10px 10px;
    background: linear-gradient(180deg, #f1d7c0, #e8b98f);
  }
  .front-brand {
    position: absolute; left: 0; right: 0; top: 190px;
    text-align: center;
    font-weight: 700; font-size: 64px; letter-spacing: 1px;
    color: var(--white);
    line-height: 1;
  }
  .front-brand .mark {
    display: inline-block; width: 22px; height: 22px; border-radius: 50%;
    background: var(--white); margin-right: 14px; vertical-align: middle;
  }
  /* Back */
  .card-back { top: 543px; background: var(--paper); }
  .back-wave { position: absolute; inset: 0; }
  .back-brand {
    position: absolute; left: 40px; top: 42px;
    font-weight: 700; font-size: 46px; color: var(--pink);
    line-height: 1;
  }
  .back-brand .mark {
    display: inline-block; width: 18px; height: 18px;
    background: var(--blue); border-radius: 50%;
    margin-right: 10px; vertical-align: middle;
  }
  .art-characters-back {
    position: absolute; left: 440px; top: 96px; width: 280px; height: 150px;
    border-radius: 70px 70px 16px 16px;
    background: linear-gradient(180deg, #f3dcc4, #e4b58c);
  }
  .contact {
    position: absolute; left: 48px; top: 210px;
    color: var(--ink-white); font-size: 17px; line-height: 1.5;
  }
  .contact .row { display: flex; align-items: center; gap: 8px; }
  .contact svg { width: 15px; height: 15px; flex: none; }
  .contact .gap { height: 8px; }
  .person {
    position: absolute; right: 52px; bottom: 44px;
    color: var(--ink-white); text-align: right;
  }
  .person-name { font-weight: 700; font-size: 24px; }
  .person-role { font-size: 18px; margin-top: 4px; }
</style>
</head>
<body>

<section class="card card-front">
  <div class="front-art art-comet" role="img" aria-label="Shooting star with glitter tail illustration"></div>
  <div class="front-art art-balloon-left" role="img" aria-label="Smiling blue balloon illustration"></div>
  <div class="front-art art-balloon-right" role="img" aria-label="Smiling pink balloon illustration"></div>
  <div class="front-art art-cloud-left" role="img" aria-label="Cloud illustration"></div>
  <div class="front-art art-cloud-right" role="img" aria-label="Cloud and star illustration"></div>
  <div class="art-characters-front" role="img" aria-label="Cartoon illustration of two toddlers peeking over the name"></div>
  <div class="front-brand"><span class="mark"></span>Poppel Hoek</div>
</section>

<section class="card card-back">
  <svg class="back-wave" viewBox="0 0 760 434" preserveAspectRatio="none" aria-hidden="true">
    <path d="M0 146 C 180 118, 360 170, 500 226 S 690 282, 760 262 L760 434 L0 434 Z" fill="var(--pink)"/>
    <path d="M0 158 C 180 130, 360 182, 500 238 S 690 294, 760 274 L760 434 L0 434 Z" fill="var(--white)"/>
    <path d="M0 164 C 180 136, 360 188, 500 244 S 690 300, 760 280 L760 434 L0 434 Z" fill="var(--blue)"/>
  </svg>
  <div class="back-brand"><span class="mark"></span>Poppel Hoek</div>
  <div class="art-characters-back" role="img" aria-label="Cartoon illustration of a girl and a waving boy peeking over the wave"></div>
  <div class="contact">
    <div>Poppel Hoek International Daycare</div>
    <div>Kastanjeweg 47 B, 2316 KR Leiden</div>
    <div class="gap"></div>
    <div class="row">
      <svg viewBox="0 0 24 24"><path fill="#fff" d="M6.6 10.8a15.1 15.1 0 0 0 6.6 6.6l2.2-2.2c.3-.3.7-.4 1-.2 1.1.4 2.3.6 3.6.6.6 0 1 .4 1 1V20c0 .6-.4 1-1 1C10.6 21 3 13.4 3 4c0-.6.4-1 1-1h3.5c.6 0 1 .4 1 1 0 1.3.2 2.5.6 3.6.1.3 0 .7-.2 1z"/></svg>
      <span>+31 647315082</span>
    </div>
    <div class="row">
      <svg viewBox="0 0 24 24"><circle cx="12" cy="12" r="9" fill="none" stroke="#fff" stroke-width="2"/><path d="M3 12h18M12 3c3 3 3 15 0 18M12 3c-3 3-3 15 0 18" fill="none" stroke="#fff" stroke-width="1.6"/></svg>
      <span>www.poppelhoek.nl</span>
    </div>
  </div>
  <div class="person">
    <div class="person-name">Lotte de Vries-Bakhuis</div>
    <div class="person-role">Communications Wizard</div>
  </div>
</section>

</body>
</html>
```